Need a design for Loan Site with new age design

We need a design for our site www.credvista.in , we deal with different verticals like home loan, personal loan, loan against property and business loans. Feel free to get in touch if you have any questions.

I have like the concept of the drop down on the eye level where consumer is able to select the product they wish and continue with the form https://www.tulsiorbit.com/ . They are in the same line of business as we are.

Here are few more designs which i personally like just to get idea about the taste

https://plumridgestudio.com/
http://zenpik.com/partners

Industry/Entity Type

Loan

Number of Pages Required

2 page

Colors
34a7d7
add136
faa54b
fbee3e

Requirements
Must have
• I have like the concept of the drop down on the eye level where consumer is able to select the product they wish and continue with the form https://www.tulsiorbit.com/ . They are in the same line of business as we are.
• Here are few more designs which i personally like just to get idea about the taste
• https://plumridgestudio.com/
• http://zenpik.com/partners

```html
<!DOCTYPE html>
<html lang="en">
<head>
<meta charset="utf-8">
<title>CredVista – Find the best loan rate</title>
<link rel="stylesheet" href="https://fonts.googleapis.com/css2?family=Lato:wght@400;700&display=swap">
<style>
:root{
  --navy:#0f5a93;
  --blue:#1a7cc4;
  --blue-mid:#2a8fd0;
  --sky:#8fb6d4;
  --red:#f65a5e;
  --red-btn:#f4473b;
  --ink:#1a4f80;
  --grey:#7a8792;
  --white:#ffffff;
}
*{box-sizing:border-box;margin:0;padding:0}
html,body{width:1021px;height:1200px;overflow:hidden;background:var(--white);font-family:'Lato',sans-serif}
.page{position:relative;width:1021px;height:1200px;overflow:hidden}

/* header */
.site-header{position:absolute;left:0;top:0;width:100%;height:72px;background:var(--white)}
.brand{position:absolute;display:flex;align-items:center;gap:8px;color:var(--navy);font-weight:400}
.brand-mark{width:28px;height:28px;background:var(--blue)}
.site-header .brand{left:133px;top:22px;font-size:19px}
.header-divider{position:absolute;left:278px;top:20px;width:2px;height:42px;background:var(--blue)}
.main-nav{position:absolute;left:297px;top:29px;display:flex;gap:14px;align-items:center;font-size:12px;font-weight:700;color:var(--navy)}
.main-nav .active{background:var(--red);color:var(--white);padding:4px 12px;border-radius:6px}
.login-icon{position:absolute;left:864px;top:26px}

/* hero */
.hero{position:absolute;left:0;top:72px;width:100%;height:398px;overflow:hidden}
.hero-art{position:absolute;left:0;top:0;width:100%;height:336px;background:linear-gradient(#b9cfe0 0%,#7ea6c8 30%,#3e7db0 60%,#155f99 85%,#0f5a93 100%)}
.hero-title{position:absolute;left:0;width:100%;top:88px;text-align:center;color:var(--white);font-weight:700;font-size:32px}
.hero-sub{position:absolute;left:0;width:100%;top:132px;text-align:center;color:var(--white);font-size:20px}
.loan-search{position:absolute;left:286px;top:186px;width:450px;height:42px;display:flex;border-radius:4px;overflow:hidden}
.loan-select{flex:0 0 177px;background:var(--white);display:flex;align-items:center;justify-content:space-between;padding:0 14px 0 12px;font-size:11px;color:var(--grey);border-right:1px solid #d7dde3}
.loan-search .search-btn{flex:1;background:var(--red);color:var(--white);font-size:16px;display:flex;align-items:center;justify-content:center}
.hero-arrows{position:absolute;left:360px;top:232px}
.hero-band{position:absolute;left:0;top:336px;width:100%;height:62px;background:var(--red)}
.mascot{position:absolute;left:452px;top:242px;width:118px;height:156px;background:linear-gradient(#f2c79a,#1f3c63);border-radius:40px 40px 8px 8px;opacity:.85}

/* partners */
.partners{position:absolute;left:0;top:470px;width:100%;height:160px}
.partners h2{position:absolute;left:0;width:100%;top:36px;text-align:center;font-size:24px;font-weight:700;color:var(--blue)}
.partners .rule{position:absolute;left:260px;top:76px;width:500px;height:1px;background:linear-gradient(90deg,transparent,#c7d3de,transparent)}
.partner-list{position:absolute;left:180px;top:88px;width:660px;display:flex;justify-content:space-between;list-style:none}
.partner{display:flex;align-items:center;gap:6px;font-size:17px;font-weight:700;color:#8a1f3a}
.partner i{width:16px;height:16px;border-radius:50%;background:#8a1f3a}

/* features */
.features-head{position:absolute;left:0;top:630px;width:100%;height:48px;background:linear-gradient(var(--blue),var(--navy))}
.features-head h2{text-align:center;color:var(--white);font-size:24px;font-weight:700;line-height:48px}
.features-head .notch{position:absolute;left:498px;top:48px;width:0;height:0;border-left:13px solid transparent;border-right:13px solid transparent;border-top:10px solid var(--navy);z-index:2}
.features{position:absolute;left:0;top:678px;width:100%;height:254px;background:linear-gradient(180deg,#d9ebf6,#f6f9fb 55%,#e8f1f7)}
.feature-list{position:absolute;left:140px;top:44px;width:740px;display:flex;list-style:none}
.feature{flex:1;text-align:center;border-left:1px solid #b9d6ea}
.feature:first-child{border-left:none}
.feature svg{display:block;margin:0 auto 14px}
.feature h3{font-size:17px;font-weight:700;color:var(--ink)}
.feature p{font-size:12px;color:var(--blue-mid);line-height:15px;font-weight:700}

/* call to action */
.cta{position:absolute;left:0;top:932px;width:100%;height:194px;background:var(--blue)}
.cta-inner{position:absolute;left:0;top:36px;width:100%;height:122px;background:#1670b6}
.cta h2{position:absolute;left:0;width:100%;top:56px;text-align:center;color:var(--white);font-size:25px;font-weight:700}
.cta .inquire-btn{position:absolute;left:445px;top:99px;width:135px;height:31px;background:var(--red-btn);color:var(--white);font-size:16px;display:flex;align-items:center;justify-content:center;border-radius:2px}
.cta-edge{position:absolute;left:0;bottom:0;width:100%;height:4px;background:#3aa1e0}

/* footer */
.site-footer{position:absolute;left:0;top:1126px;width:100%;height:74px}
.site-footer .brand{left:170px;top:22px;font-size:12px;gap:6px}
.site-footer .brand-mark{width:20px;height:20px}
.footer-legal{position:absolute;right:159px;top:28px;font-size:10px;color:var(--ink);font-weight:700}
.footer-legal span{color:var(--blue-mid);margin-left:8px;font-weight:400}
</style>
</head>
<body>
<div class="page">

  <header class="site-header">
    <div class="brand"><span class="brand-mark"></span>CredVista</div>
    <span class="header-divider"></span>
    <nav class="main-nav">
      <span class="active">Home</span><span>Who We Are</span><span>Services</span><span>Blog</span><span>Career</span><span>Reach Us</span>
    </nav>
    <svg class="login-icon" width="32" height="34" viewBox="0 0 32 34" aria-label="Log in">
      <path d="M12 3h15a2 2 0 0 1 2 2v24a2 2 0 0 1-2 2H12" fill="none" stroke="#0f5a93" stroke-width="3.5"/>
      <path d="M2 17h14M11 11l6 6-6 6" fill="none" stroke="#0f5a93" stroke-width="3.5"/>
    </svg>
  </header>

  <section class="hero">
    <div class="hero-art" role="img" aria-label="Illustrated sky of soft clouds over faint money and finance icons"></div>
    <h1 class="hero-title">Looking for a secured or unsecured loan</h1>
    <p class="hero-sub">We will help you get the best interest rate</p>
    <div class="loan-search">
      <div class="loan-select">I would like to
        <svg width="14" height="8" viewBox="0 0 14 8"><path d="M1 1l6 6 6-6" fill="none" stroke="#f65a5e" stroke-width="2"/></svg></div>
      <div class="loan-select">Select a Product
        <svg width="14" height="8" viewBox="0 0 14 8"><path d="M1 1l6 6 6-6" fill="none" stroke="#f65a5e" stroke-width="2"/></svg></div>
      <div class="search-btn">Search</div>
    </div>
    <div class="hero-band" role="img" aria-label="Red band with faint loan type icons"></div>
    <svg class="hero-arrows" width="310" height="110" viewBox="0 0 310 110" aria-hidden="true">
      <path d="M42 100C20 70 10 40 18 4M6 16L18 4l14 10" fill="none" stroke="#fff" stroke-width="3"/>
      <path d="M262 100c22-30 32-60 24-96M274 16L286 4l-14 10" fill="none" stroke="#fff" stroke-width="3"/>
    </svg>
    <div class="mascot" role="img" aria-label="Cheerful cartoon loan advisor in a suit waving both hands"></div>
  </section>

  <section class="partners">
    <h2>We work with all premium Financial Institutions</h2>
    <span class="rule"></span>
    <ul class="partner-list">
      <li class="partner"><i></i>Norvale Bank</li>
      <li class="partner">Kestrin Bank</li>
      <li class="partner"><i></i>Ardent Bank</li>
      <li class="partner"><i></i>Pellor Finserv</li>
      <li class="partner"><i></i>Tamsy</li>
    </ul>
  </section>

  <div class="features-head"><h2>Features</h2><span class="notch"></span></div>
  <section class="features" role="img" aria-label="Soft background photo of a handshake">
    <ul class="feature-list">
      <li class="feature">
        <svg width="80" height="100" viewBox="0 0 80 100" aria-hidden="true">
          <rect x="6" y="10" width="68" height="86" rx="6" fill="none" stroke="#1a8cc9" stroke-width="5"/>
          <rect x="26" y="2" width="28" height="14" rx="3" fill="#1a5f94"/>
          <circle cx="22" cy="40" r="6" fill="#1a8cc9"/><rect x="12" y="48" width="20" height="8" rx="3" fill="#1a8cc9"/>
          <path d="M38 38h26M38 48h26M14 66h50M14 76h50" stroke="#1a8cc9" stroke-width="4"/>
        </svg>
        <h3>Easy Documentation</h3>
      </li>
      <li class="feature">
        <svg width="110" height="100" viewBox="0 0 110 100" aria-hidden="true">
          <rect x="4" y="34" width="62" height="46" fill="#1a8cc9"/>
          <path d="M66 44h22l16 18v18H66Z" fill="#1a8cc9"/>
          <circle cx="26" cy="24" r="20" fill="#fff" stroke="#1a5f94" stroke-width="5"/>
          <path d="M26 12v12h9" stroke="#1a5f94" stroke-width="4" fill="none"/>
          <circle cx="24" cy="84" r="10" fill="#1a5f94"/><circle cx="86" cy="84" r="10" fill="#1a5f94"/>
        </svg>
        <h3>Doorstep Deliveries</h3>
      </li>
      <li class="feature">
        <svg width="104" height="100" viewBox="0 0 104 100" aria-hidden="true">
          <path d="M6 4h40l14 14v52H6Z" fill="none" stroke="#1a8cc9" stroke-width="6"/>
          <path d="M44 30h40l14 14v52H44Z" fill="#fff" stroke="#1a5f94" stroke-width="6"/>
          <path d="M14 40h24M30 32l10 8-10 8" stroke="#1a8cc9" stroke-width="5" fill="none"/>
          <path d="M90 64H64M72 56l-10 8 10 8" stroke="#1a5f94" stroke-width="5" fill="none"/>
        </svg>
        <h3>Compare Quote</h3>
        <p>from all major<br>financial institutions</p>
      </li>
      <li class="feature">
        <svg width="100" height="100" viewBox="0 0 100 100" aria-hidden="true">
          <rect x="6" y="10" width="64" height="84" rx="4" fill="none" stroke="#1a5f94" stroke-width="5"/>
          <rect x="24" y="4" width="28" height="12" rx="3" fill="#1a5f94"/>
          <path d="M16 34l4 4 7-7M16 52l4 4 7-7M16 70l4 4 7-7M34 35h26M34 53h20M34 71h14" stroke="#1a8cc9" stroke-width="3.5" fill="none"/>
          <circle cx="72" cy="72" r="22" fill="#fff" stroke="#1a8cc9" stroke-width="6"/>
          <path d="M61 72l8 8 14-14" stroke="#1a8cc9" stroke-width="6" fill="none"/>
        </svg>
        <h3>Get Approval</h3>
        <p>within 7 business days</p>
      </li>
    </ul>
  </section>

  <section class="cta">
    <div class="cta-inner"></div>
    <h2>What Are You Waiting For?</h2>
    <div class="inquire-btn">Inquire Now</div>
    <span class="cta-edge"></span>
  </section>

  <footer class="site-footer">
    <div class="brand"><span class="brand-mark"></span>CredVista</div>
    <p class="footer-legal">Copyright © 2016 CredVista<span>Privacy Policy</span></p>
  </footer>

</div>
</body>
</html>
```